Trade Show Banner "Brindlequay"

1.7' x 3' vertical banner to complement trade show booth panels (3-panel tabletop booth attached). The word file (attached) is for text and not meant to imply design. We manage homeowner and condo associations that are run by volunteer boards of directors who already have full-time jobs or who may have no training in how to run an organization. It can be highly stressful and not very rewarding. We want this poster/banner to convey that feeling of stress along with a hope for relief and relaxation. Our logo is attached. The full logo is the top one in the file. You may also want to use the triangle (attached) in addition to or instead of the logo. Our corporate fonts are attached. Please let me know if you need additional information or if you feel like there is too much copy or any other thoughts or comments you have.

Target Market(s)

Volunteer boards of directors for homeowner and condo associations--all ages, genders, races, occupations.

Industry/Entity Type

Property Management

Other font styles liked:
• "Copper Lantern" is part of a trademark and should be in Mistral with the green from our logo

Requirements
Must have
• Simple, easy to read, don't clash with booth design
Nice to have
• convey the tension of stress contrasted with the feeling of relaxation and relief.

```html
<!DOCTYPE html>
<html lang="en">
<head>
<meta charset="utf-8">
<title>The Art of Brindlequay for Board Members</title>
<link rel="stylesheet" href="https://fonts.googleapis.com/css2?family=Pacifico&family=Caveat:wght@500&family=Noto+Sans:wght@400;700&family=Questrial&display=swap">
<style>
  :root {
    --green: #1f7a40;
    --green-deep: #196a36;
    --maroon: #7a1020;
    --ink: #1a1a1a;
    --white: #ffffff;
  }
  * { margin: 0; padding: 0; box-sizing: border-box; }
  html, body { width: 1200px; height: 2273px; overflow: hidden; background: var(--white); }
  .banner { position: relative; width: 1200px; height: 2273px; overflow: hidden; background: var(--white); font-family: "Noto Sans", Verdana, sans-serif; color: var(--ink); }
  .banner__shapes { position: absolute; inset: 0; }
  .headline { position: absolute; left: 152px; top: 92px; color: var(--white); }
  .headline__lead { font-family: "Questrial", "Century Gothic", sans-serif; font-size: 80px; line-height: 1; letter-spacing: 1px; }
  .headline__script { font-family: "Pacifico", cursive; font-size: 172px; line-height: 1.1; margin: -6px 0 0 50px; }
  .headline__tail { font-family: "Questrial", "Century Gothic", sans-serif; font-size: 62px; line-height: 1; margin: -18px 0 0 6px; }
  .headline__tail em { font-style: italic; }
  .stress-list { position: absolute; left: 95px; top: 762px; width: 1070px; }
  .stress { margin-bottom: 30px; }
  .stress__problem { font-weight: 700; font-size: 34px; line-height: 1.3; }
  .stress__relief { font-size: 36px; line-height: 1.32; }
  .stress__relax { font-family: "Pacifico", cursive; color: var(--green); font-size: 46px; line-height: 1; margin-right: 6px; }
  .stress__brand { font-family: "Caveat", cursive; color: var(--green); font-size: 46px; }
  .company { position: absolute; left: 96px; top: 1808px; display: flex; align-items: center; gap: 22px; }
  .company__mark { width: 62px; height: 62px; background: var(--maroon); }
  .company__name { font-family: "Noto Sans", Verdana, sans-serif; font-weight: 700; font-size: 40px; color: var(--ink); }
  .cta { position: absolute; left: 729px; top: 1835px; width: 420px; height: 420px; border-radius: 50%; background: var(--maroon); border: 16px solid var(--white); display: flex; align-items: center; justify-content: center; }
  .cta__text { transform: rotate(-14deg); color: var(--white); font-family: "Noto Sans", Verdana, sans-serif; font-weight: 700; font-size: 46px; line-height: 1.08; text-align: center; text-transform: uppercase; }
</style>
</head>
<body>
<main class="banner">
  <svg class="banner__shapes" width="1200" height="2273" viewBox="0 0 1200 2273" aria-hidden="true">
    <path class="top-field" fill="var(--green)" d="M0 0H1200V392C1100 520 900 560 650 580C400 600 200 625 92 712L0 745Z"/>
    <path class="top-swoosh" fill="var(--maroon)" d="M92 712C200 625 400 600 650 580C900 560 1100 520 1200 392V470C1100 585 900 620 650 632C420 644 220 660 92 712Z"/>
    <path class="bottom-field" fill="var(--green)" d="M1200 1920C1150 2060 1000 2160 780 2215C620 2250 470 2262 360 2273H1200Z"/>
    <path class="bottom-swoosh" fill="var(--maroon)" d="M0 2200C180 2160 420 2185 620 2230C700 2246 780 2262 860 2273H0Z"/>
  </svg>

  <header class="headline">
    <div class="headline__lead">THE ART OF</div>
    <div class="headline__script">Brindlequay</div>
    <div class="headline__tail"><em>for</em> BOARD MEMBERS</div>
  </header>

  <section class="stress-list">
    <div class="stress">
      <p class="stress__problem">Stress: THE BOARD HAS TOO MUCH WORK TO DO</p>
      <p class="stress__relief"><span class="stress__relax">Relax...</span> and let us do the work.</p>
    </div>
    <div class="stress">
      <p class="stress__problem">Stress: YOUR COMMUNITY HAS “ISSUES.”</p>
      <p class="stress__relief"><span class="stress__relax">Relax...</span> and let us give you a <span class="stress__brand">Copper Lantern.</span></p>
    </div>
    <div class="stress">
      <p class="stress__problem">Stress: YOUR MEMBERS CANNOT PAY ONLINE.</p>
      <p class="stress__relief"><span class="stress__relax">Relax...</span> we’ll give your members multiple ways to pay.</p>
    </div>
    <div class="stress">
      <p class="stress__problem">Stress: COMMUNICATION IS POOR OR INCONSISTENT.</p>
      <p class="stress__relief"><span class="stress__relax">Relax...</span> we’ll keep you informed with a robust online portal, chock full of information.</p>
    </div>
    <div class="stress">
      <p class="stress__problem">Stress: YOUR DELINQUENCIES ARE HIGH.</p>
      <p class="stress__relief"><span class="stress__relax">Relax...</span> as a licensed collection agency, we have developed an effective collections program that works in tandem with your collections attorney. Plus, we can report to the credit bureau!</p>
    </div>
  </section>

  <div class="company">
    <span class="company__mark"></span>
    <span class="company__name">Harrowgate Management, Inc.</span>
  </div>

  <div class="cta">
    <p class="cta__text">Come in<br>to talk<br>and start<br>relaxing<br>today!</p>
  </div>
</main>
</body>
</html>
```